Fun, Clean Business Card For Family Focused Travel Agency

I need a business card using specific colors and fonts as in the uploaded files. Ideally, I would like a large image of the logo on the back and all the contact info on the front. Maybe the stars/dots somewhere in a flowy form.

I do want it the contact information to be clear and easy to read. I don't want it to look too busy. Maybe even a bit minimalist.

I plan or ordering the ROUNDED CORNER business cards from Cardwell Press, so please consider that in your design.

Target Market(s)

Families with children, couples, groups of friends

Contact Information for Business Card

Marla Quent, Owner
Marla@TidewayTrips.example
Cell Phone Number 555-218-6034
Office Phone Number 555-647-1295
Specializing in Fablecrest destinations, Goldmere Parkside Resort, Cruises and All-Inclusive Vacations.

Nice but not required:
www.TidewayTrips.example
Facebook, Instagram, Twitter icons with username: TidewayTrips

Font styles to use
Sans Serif

Requirements
Must have
• Please try to use the colors from the logo as much as possible. I understand lighter shades/colors may be needed for some things.
Should not have
• NO SERIF FONTS. That is really the only thing I do not want at all

```html
<!DOCTYPE html>
<html lang="en">
<head>
<meta charset="utf-8">
<title>Tideway Trips – Business Card</title>
<link href="https://fonts.googleapis.com/css2?family=Roboto:wght@400;500;700&display=swap" rel="stylesheet">
<style>
  :root {
    --sun: #f7d80e;
    --sun-deep: #e9c700;
    --charcoal: #2b2b2b;
    --charcoal-deep: #232323;
    --ink: #1b1d2a;
    --white: #f4f4f4;
    --stage: #e6e8e4;
  }
  * { box-sizing: border-box; margin: 0; padding: 0; }
  html, body { width: 1200px; height: 781px; overflow: hidden; }
  body {
    background: var(--stage);
    font-family: "Roboto", Arial, sans-serif;
    position: relative;
  }
  .card {
    position: absolute;
    border-radius: 22px;
    overflow: hidden;
    box-shadow: 0 6px 18px rgba(0,0,0,.18);
  }
  /* Front: contact side */
  .card-front {
    left: 110px; top: 80px; width: 360px; height: 620px;
    background: var(--charcoal);
  }
  .front-top {
    position: absolute; left: 0; top: 0; width: 100%; height: 262px;
    background: radial-gradient(circle at 55% 35%, #fde54a, var(--sun) 55%, var(--sun-deep));
    border-bottom: 3px solid var(--sun);
  }
  .brand-small {
    position: absolute; left: 40px; top: 70px;
    display: flex; align-items: center; gap: 12px;
  }
  .brand-dot { width: 38px; height: 38px; border-radius: 50%; background: var(--ink); }
  .brand-name-small { font-size: 30px; font-weight: 700; color: var(--ink); }
  .tagline {
    position: absolute; left: 40px; top: 130px; width: 250px;
    font-size: 12px; line-height: 17px; color: var(--ink);
  }
  .front-bottom { position: absolute; left: 0; top: 262px; width: 100%; height: 358px; }
  .rail {
    position: absolute; left: 56px; top: 0; width: 2px; height: 100%;
    background: var(--sun);
  }
  .rail-dots { position: absolute; left: 45px; top: 48px; display: flex; flex-direction: column; gap: 14px; }
  .rail-dot { width: 24px; height: 24px; border-radius: 50%; background: var(--sun); border: 3px solid var(--charcoal); }
  .handle {
    position: absolute; left: 30px; top: 185px;
    writing-mode: vertical-rl; font-size: 15px; font-weight: 700; color: var(--sun);
  }
  .person { position: absolute; left: 96px; top: 34px; right: 20px; }
  .person-name { font-size: 36px; font-weight: 700; color: var(--white); letter-spacing: .5px; }
  .website { font-size: 15px; color: #cfcfcf; margin-top: 4px; }
  .contacts { list-style: none; margin-top: 34px; display: flex; flex-direction: column; gap: 20px; }
  .contact { display: flex; align-items: center; gap: 14px; font-size: 13.5px; color: #e2e2e2; }
  .contact svg { width: 20px; height: 20px; flex: none; }

  /* Back: brand side */
  .card-back {
    left: 520px; top: 220px; width: 620px; height: 350px;
    background: radial-gradient(circle at 40% 35%, #fde54a, var(--sun) 50%, var(--sun-deep));
  }
  .brand-large {
    position: absolute; left: 0; top: 0; width: 100%; height: 100%;
    display: flex; align-items: center; justify-content: center; gap: 22px;
  }
  .brand-circle { width: 90px; height: 90px; border-radius: 50%; background: var(--ink); }
  .brand-name-large { font-size: 64px; font-weight: 700; color: var(--ink); }
</style>
</head>
<body>
  <section class="card card-front" aria-label="Card front">
    <div class="front-top">
      <div class="brand-small">
        <span class="brand-dot"></span>
        <span class="brand-name-small">Tideway Trips</span>
      </div>
      <p class="tagline">Specializing in Fablecrest destinations, Goldmere Parkside Resort, Cruises and All-Inclusive Vacations.</p>
    </div>
    <div class="front-bottom">
      <span class="rail"></span>
      <div class="rail-dots">
        <span class="rail-dot"></span><span class="rail-dot"></span><span class="rail-dot"></span>
      </div>
      <span class="handle">TidewayTrips</span>
      <div class="person">
        <h1 class="person-name">Marla Quent</h1>
        <p class="website">www.TidewayTrips.example</p>
        <ul class="contacts">
          <li class="contact">
            <svg viewBox="0 0 20 20" fill="none" stroke="#e2e2e2" stroke-width="1.6"><rect x="2" y="4" width="16" height="12" rx="1"/><path d="M2 5l8 6 8-6"/></svg>
            Marla@TidewayTrips.example
          </li>
          <li class="contact">
            <svg viewBox="0 0 20 20" fill="#e2e2e2"><rect x="2" y="5" width="4" height="12" rx="1"/><rect x="7" y="3" width="11" height="14" rx="1.5"/><rect x="9" y="5" width="7" height="3" fill="#2b2b2b"/><circle cx="10" cy="11" r="1" fill="#2b2b2b"/><circle cx="13" cy="11" r="1" fill="#2b2b2b"/><circle cx="10" cy="14" r="1" fill="#2b2b2b"/><circle cx="13" cy="14" r="1" fill="#2b2b2b"/></svg>
            Office Phone 555-647-1295
          </li>
          <li class="contact">
            <svg viewBox="0 0 20 20" fill="none" stroke="#e2e2e2" stroke-width="1.6"><rect x="5.5" y="2" width="9" height="16" rx="1.8"/><path d="M9 15.5h2"/></svg>
            Cell Phone 555-218-6034
          </li>
        </ul>
      </div>
    </div>
  </section>

  <section class="card card-back" aria-label="Card back">
    <div class="brand-large">
      <span class="brand-circle"></span>
      <span class="brand-name-large">Tideway Trips</span>
    </div>
  </section>
</body>
</html>
```